Crossword App Main Page Design

For a crossword application we need a main page. I am enclosing the current temporary design. There will be 5 buttons. We want a simple but attractive design. Vector designs are preferred. Thank you very much for your interest.
The name of the application is Polyglyph Gridword Riddle and the motto is "gridplay rebuilt." So please use this name on the screen.
Thwe designs I have received so far almost the same with one I have attached. Only the button colors and background image are different. Please try different placement and buttons.
Thanks

```html
<!DOCTYPE html>
<html lang="en">
<head>
<meta charset="utf-8">
<title>Polyglyph Gridword Riddle – Main Page</title>
<link rel="stylesheet" href="https://fonts.googleapis.com/css2?family=Libre+Baskerville:wght@700&family=Roboto:wght@400;700&display=swap">
<style>
  :root {
    --screen-bg: #0b0d0e;
    --grid-dark: #1a2022;
    --grid-mid: #273033;
    --status-bg: #141616;
    --text-light: #f2f2f2;
    --text-muted: #8a8d8e;
    --tile-top: #2e3638;
    --tile-bottom: #121617;
    --tile-edge: #3c4446;
    --icon-gray: #b4b8b9;
    --accent-blue: #3aa8e6;
    --button-top: #4b6a70;
    --button-bottom: #0f1516;
  }
  html, body {
    margin: 0;
    padding: 0;
    width: 685px;
    height: 1200px;
    overflow: hidden;
    background: var(--screen-bg);
  }
  .app-screen {
    position: relative;
    width: 685px;
    height: 1200px;
    background: var(--screen-bg);
    overflow: hidden;
    font-family: "Roboto", Arial, sans-serif;
  }
  .grid-backdrop {
    position: absolute;
    inset: 50px 0 0 0;
    background:
      linear-gradient(180deg, rgba(11,13,14,0.95) 0%, rgba(11,13,14,0.5) 40%, rgba(11,13,14,0.3) 100%),
      linear-gradient(180deg, var(--grid-dark) 0%, var(--grid-mid) 100%);
  }
  .status-bar {
    position: absolute;
    top: 0; left: 0; right: 0;
    height: 50px;
    background: var(--status-bg);
    display: flex;
    align-items: center;
    padding: 0 16px;
    box-sizing: border-box;
    color: #e8e8e8;
    font-weight: 700;
    font-size: 24px;
  }
  .status-bar .signal { margin-right: 8px; }
  .status-bar .network { margin-left: 18px; }
  .status-bar .battery { margin-left: auto; }
  .app-title {
    position: absolute;
    top: 112px;
    left: 0; right: 0;
    margin: 0;
    text-align: center;
    font-family: "Libre Baskerville", "Times New Roman", serif;
    font-weight: 700;
    font-size: 38px;
    color: var(--text-light);
  }
  .app-motto {
    position: absolute;
    top: 172px;
    left: 0; right: 0;
    margin: 0;
    text-align: center;
    font-size: 18px;
    letter-spacing: 8px;
    color: var(--text-muted);
  }
  .play-button {
    position: absolute;
    left: 252px;
    top: 250px;
    width: 180px;
    height: 180px;
    border-radius: 34px;
    border: 4px solid #000;
    box-sizing: border-box;
    background: linear-gradient(180deg, var(--button-top) 0%, #1d2a2d 50%, var(--button-bottom) 100%);
    box-shadow: 0 0 0 2px var(--tile-edge), 0 8px 18px rgba(0,0,0,0.7);
    display: flex;
    align-items: center;
    justify-content: center;
  }
  .menu-grid {
    position: absolute;
    left: 40px;
    right: 40px;
    top: 500px;
    display: grid;
    grid-template-columns: 1fr 1fr;
    gap: 25px;
  }
  .menu-tile {
    height: 300px;
    border-radius: 22px;
    background: linear-gradient(180deg, var(--tile-top) 0%, var(--tile-bottom) 100%);
    box-shadow: inset 0 0 0 2px var(--tile-edge), 0 6px 14px rgba(0,0,0,0.6);
    display: flex;
    flex-direction: column;
    align-items: center;
    justify-content: center;
    gap: 22px;
    color: var(--text-light);
    font-weight: 700;
    font-size: 26px;
  }
  .menu-tile svg { width: 96px; height: 96px; }
  .menu-tile--active {
    box-shadow: inset 0 0 0 3px var(--accent-blue), 0 6px 14px rgba(0,0,0,0.6);
  }
</style>
</head>
<body>
<main class="app-screen">
  <div class="grid-backdrop" role="img" aria-label="Faint crossword grid backdrop with numbered squares"></div>

  <header class="status-bar">
    <svg class="signal" width="40" height="18" viewBox="0 0 40 18" aria-hidden="true">
      <rect x="0" y="13" width="5" height="5" fill="#e8e8e8"/>
      <rect x="8" y="10" width="5" height="8" fill="#e8e8e8"/>
      <rect x="16" y="7" width="5" height="11" fill="#e8e8e8"/>
      <rect x="24" y="3" width="5" height="15" fill="#e8e8e8"/>
      <rect x="32" y="0" width="5" height="18" fill="#e8e8e8"/>
    </svg>
    <span class="carrier">NIMBUS</span>
    <span class="network">3G</span>
    <svg class="battery" width="42" height="20" viewBox="0 0 42 20" aria-hidden="true">
      <rect x="1" y="1" width="36" height="18" rx="3" fill="none" stroke="#e8e8e8" stroke-width="2"/>
      <rect x="4" y="4" width="30" height="12" rx="1" fill="#e8e8e8"/>
      <rect x="38" y="6" width="3" height="8" fill="#e8e8e8"/>
    </svg>
  </header>

  <h1 class="app-title">Polyglyph Gridword Riddle</h1>
  <p class="app-motto">gridplay rebuilt.</p>

  <div class="play-button" aria-label="Play">
    <svg width="84" height="94" viewBox="0 0 80 90" aria-hidden="true">
      <defs>
        <linearGradient id="playArrow" x1="0" y1="0" x2="0" y2="1">
          <stop offset="0" stop-color="#ffffff"/>
          <stop offset="1" stop-color="#b9c2c4"/>
        </linearGradient>
      </defs>
      <path d="M12 6 L72 45 L12 84 Z" fill="url(#playArrow)" stroke="#dfe5e6" stroke-width="3" stroke-linejoin="round"/>
    </svg>
  </div>

  <nav class="menu-grid">
    <div class="menu-tile">
      <svg viewBox="0 0 52 52" aria-hidden="true">
        <path d="M26 46 C10 34 4 26 4 17 C4 10 9 5 16 5 C20 5 24 8 26 12 C28 8 32 5 36 5 C43 5 48 10 48 17 C48 26 42 34 26 46 Z" fill="var(--icon-gray)"/>
      </svg>
      <span>Play</span>
    </div>
    <div class="menu-tile menu-tile--active">
      <svg viewBox="0 0 52 52" aria-hidden="true">
        <path d="M26 4 C18 9 11 10 6 10 C6 30 12 42 26 48 C40 42 46 30 46 10 C41 10 34 9 26 4 Z" fill="var(--accent-blue)"/>
        <path d="M26 11 C20 14 15 15 12 15 C13 30 17 38 26 42 C35 38 39 30 40 15 C37 15 32 14 26 11 Z" fill="#1c2f3a"/>
      </svg>
      <span>My Puzzles</span>
    </div>
    <div class="menu-tile">
      <svg viewBox="0 0 52 52" aria-hidden="true">
        <path d="M3 8 H11 L17 34 H42 L47 15 H14" fill="none" stroke="var(--icon-gray)" stroke-width="4" stroke-linejoin="round"/>
        <circle cx="20" cy="42" r="4" fill="var(--icon-gray)"/>
        <circle cx="39" cy="42" r="4" fill="var(--icon-gray)"/>
      </svg>
      <span>Buy Puzzles</span>
    </div>
    <div class="menu-tile">
      <svg viewBox="0 0 52 52" aria-hidden="true">
        <g fill="var(--icon-gray)">
          <circle cx="26" cy="26" r="15"/>
          <rect x="22" y="4" width="8" height="10"/>
          <rect x="22" y="38" width="8" height="10"/>
          <rect x="4" y="22" width="10" height="8"/>
          <rect x="38" y="22" width="10" height="8"/>
          <rect x="22" y="4" width="8" height="10" transform="rotate(45 26 26)"/>
          <rect x="22" y="38" width="8" height="10" transform="rotate(45 26 26)"/>
          <rect x="4" y="22" width="10" height="8" transform="rotate(45 26 26)"/>
          <rect x="38" y="22" width="10" height="8" transform="rotate(45 26 26)"/>
        </g>
        <circle cx="26" cy="26" r="6" fill="#1a1f20"/>
      </svg>
      <span>Setttings</span>
    </div>
  </nav>
</main>
</body>
</html>
```